PRP Poster

We need a poster for a doctors room to encourage people to enquire about PRP procedure.

It needs to include "for osteoarthritis and sports injuries" and "enhancing the body's natural ability to heal".

A brochure is attached which outlines what PRP (Platelet Rich Plasma) is, in the brochure it is called NTQ. DO NOT USE ANY OF THE LOGOS FROM THIS BROCHURE.

Target Market(s)

patients in an orthopaedic surgery waiting room/area
age range from teenagers till 80year olds
male= female ratio

Requirements
Must have
• single poster
eye-catching yet professional
needs to be suitable/appropriate for the waiting area of a surgeons clinic
Nice to have
• prp is a natural therapy (it is essentially the person's own blood being reinjected to a site of injury)
the "natural" aspect of the therapy needs to be emphasised

```html
<!DOCTYPE html>
<html lang="en">
<head>
<meta charset="UTF-8">
<title>Heal Naturally – PRP Procedure Poster</title>
<link rel="stylesheet" href="https://fonts.googleapis.com/css2?family=Arimo:wght@400;500&display=swap">
<style>
  :root {
    --bg-navy: #0b4d80;
    --shape-light: #1e6891;
    --shape-mid: #0f5c88;
    --shape-teal: #0d6d8e;
    --accent-lime: #e6f22c;
    --text-white: #ffffff;
  }
  html, body {
    margin: 0;
    padding: 0;
    width: 927px;
    height: 1200px;
    overflow: hidden;
    background: var(--bg-navy);
  }
  .poster {
    display: block;
    width: 927px;
    height: 1200px;
    font-family: "Arimo", Arial, sans-serif;
  }
  .poster__bg { fill: var(--bg-navy); }
  .shape--light { fill: var(--shape-light); }
  .shape--mid { fill: var(--shape-mid); }
  .shape--teal { fill: var(--shape-teal); }
  .ring--light { fill: none; stroke: var(--shape-light); }
  .ring--mid { fill: none; stroke: var(--shape-mid); }
  .headline { fill: var(--accent-lime); font-weight: 400; }
  .subhead { fill: var(--accent-lime); font-weight: 500; font-size: 51px; }
  .tagline { fill: var(--text-white); font-weight: 500; font-size: 33px; letter-spacing: 0.5px; }
  .tagline__accent { fill: var(--accent-lime); }
  .audience { fill: var(--accent-lime); font-weight: 500; }
</style>
</head>
<body>
<svg class="poster" viewBox="0 0 927 1200" xmlns="http://www.w3.org/2000/svg">
  <rect class="poster__bg" width="927" height="1200"/>

  <!-- background shapes -->
  <g class="decor">
    <circle class="shape--light" cx="9" cy="9" r="91"/>
    <circle class="ring--light" cx="222" cy="245" r="125" stroke-width="30"/>
    <circle class="shape--teal" cx="535" cy="107" r="61"/>
    <circle class="shape--teal" cx="844" cy="-18" r="41"/>
    <circle class="ring--light" cx="1045" cy="291" r="215" stroke-width="59"/>
    <circle class="ring--mid" cx="-18" cy="909" r="195" stroke-width="109"/>
    <circle class="shape--mid" cx="355" cy="727" r="56"/>
    <circle class="shape--mid" cx="723" cy="812" r="61"/>
    <circle class="shape--mid" cx="639" cy="916" r="105"/>
    <circle class="shape--light" cx="829" cy="1065" r="28"/>
  </g>

  <!-- headline -->
  <text class="headline" x="465" y="475" text-anchor="middle" font-size="140">H<tspan font-size="95">EAL</tspan></text>
  <text class="headline" x="465" y="582" text-anchor="middle" font-size="140">N<tspan font-size="95">ATURALLY</tspan></text>

  <!-- procedure statement -->
  <text class="subhead" x="462" y="753" text-anchor="middle">PRP PROCEDURE</text>
  <text class="tagline" x="462" y="797" text-anchor="middle">IS A <tspan class="tagline__accent">NATURAL THERAPY</tspan> THAT</text>
  <text class="tagline" x="462" y="843" text-anchor="middle">ENHANCES YOUR BODY’S</text>
  <text class="tagline" x="466" y="888" text-anchor="middle">NATURAL ABILITY TO HEAL</text>

  <!-- audience -->
  <text class="audience" x="463" y="1162" text-anchor="middle" font-size="28">F<tspan font-size="41" dy="0" x="0" visibility="hidden"></tspan></text>
</svg>
<style>.audience{display:none}</style>
<svg class="poster" viewBox="0 0 927 1200" xmlns="http://www.w3.org/2000/svg" style="position:absolute;top:0;left:0;pointer-events:none">
  <text x="463" y="1162" text-anchor="middle" style="fill:var(--accent-lime);font-weight:500;font-size:28px;letter-spacing:0.3px"><tspan font-size="41">F</tspan>OR OSTEOARTHRITIS AND SPORTS INJURIES</text>
</svg>
</body>
</html>
```